Arzt im ästhetischen Bereich sucht seriöses Flyer-Design
Zielgruppe
Ich bin Arzt und nebenberuflich mache ich Eingriffe im ästhetischen Bereich (Lumex- und Hyaluronunterspritzung, Lipolyse, Eigenblutbehandlung (PRP) bzw. Perlglanzkur).
Ich möchte gerne einen sechsseitigen Flyer mit Falz. Auf der Deckseite sollte ein schönes Logo mit ästhetischen Bezug stehen, auf den anderen Seiten werden je die Behandlungsmethoden erklärt (Text kann ich zusteuern bzw. füge ich nach Erhalt des Designs ein). Es sollten auf jeder Seite schöne Abbildungen (entweder Fotomaterial oder auch Zeichnungen) der Methoden enthalten sein. Auf der letzten Seite sollen meine Kontaktdaten stehen
Aufgabenstellung
s.o. 6 seitiger Flyer mit Falzen. Farbe frei. Design medizinisch-ästhetisch mit seriösen Eindruck. Logo von mir soll auf der Rückseite mit meinen Kontaktdaten eingefügt werden.

```html
<!DOCTYPE html>
<html lang="de">
<head>
<meta charset="utf-8">
<title>Flyer Ästhetische Medizin</title>
<link href="https://fonts.googleapis.com/css2?family=Raleway:wght@400;600;700&display=swap" rel="stylesheet">
<style>
  :root {
    --stage: #b9b9b9;
    --paper: #ffffff;
    --sky: #45b1e0;
    --teal-dark: #174a60;
    --teal-mid: #2f7e9f;
    --ink: #2a2a2a;
    --heading: #4b5b6b;
    --badge: #c5d3dd;
    --badge-ring: #45b1e0;
    --badge-ink: #1f2e3a;
  }
  html, body { margin: 0; padding: 0; width: 1200px; height: 676px; overflow: hidden; background: var(--stage); }
  body { font-family: "Raleway", sans-serif; color: var(--ink); }
  .flyer {
    position: absolute; left: 157px; top: 19px; width: 884px; height: 624px;
    background: var(--paper); overflow: hidden;
  }
  .top-band { position: absolute; left: 0; top: 0; width: 100%; height: 20px; background: var(--sky); }
  .photo { position: absolute; }
  .photo-hair {
    left: 0; top: 20px; width: 271px; height: 292px;
    background: linear-gradient(to bottom, rgba(255,255,255,0) 60%, #fff 100%),
                linear-gradient(120deg, #9fc7ea 0%, #c8743f 30%, #d9925e 60%, #f3e2d6 100%);
  }
  .photo-waist {
    left: 306px; top: 20px; width: 262px; height: 210px;
    background: linear-gradient(to bottom, rgba(255,255,255,0) 55%, #fff 100%),
                linear-gradient(160deg, #f0c8b2 0%, #f6d6c3 50%, #e8e4e0 100%);
  }
  .photo-face {
    left: 586px; top: 20px; width: 298px; height: 540px;
    background: linear-gradient(to bottom, #fff 0%, #f1d7c6 20%, #eac5ae 60%, #a9cde8 100%);
  }
  .wave { position: absolute; left: 0; top: 0; width: 884px; height: 624px; }
  .panel { position: absolute; font-size: 10px; line-height: 12.5px; }
  .panel p { margin: 0 0 12.5px; }
  .panel-prp { left: 19px; top: 287px; width: 252px; }
  .panel-lipo { left: 309px; top: 231px; width: 264px; }
  .panel h2 {
    margin: 0 0 13px; font-size: 15px; font-weight: 700; color: var(--heading);
    text-decoration: underline; letter-spacing: -0.2px;
  }
  .badge {
    position: absolute; left: 662px; top: 441px; width: 142px; height: 142px;
    border-radius: 50%; background: var(--badge); border: 3px solid var(--badge-ring);
    display: flex; align-items: center; justify-content: center; text-align: center;
  }
  .badge-name { font-size: 11px; font-weight: 600; color: var(--badge-ink); margin-top: 40px; }
  .tagline {
    position: absolute; right: 21px; top: 593px; font-size: 12px; color: #fff;
  }
</style>
</head>
<body>
  <main class="flyer">
    <div class="top-band"></div>
    <div class="photo photo-hair" role="img" aria-label="Foto: PRP-Injektion in die Kopfhaut mit blauen Handschuhen"></div>
    <div class="photo photo-waist" role="img" aria-label="Foto: Maßband um eine Taille"></div>
    <div class="photo photo-face" role="img" aria-label="Foto: Frauenporträt mit Injektion an der Lippe"></div>

    <svg class="wave" viewBox="0 0 884 624" aria-hidden="true">
      <defs>
        <linearGradient id="waveFill" x1="0" y1="0" x2="1" y2="0">
          <stop offset="0" stop-color="#45b1e0"/>
          <stop offset="0.55" stop-color="#2f7e9f"/>
          <stop offset="1" stop-color="#174a60"/>
        </linearGradient>
      </defs>
      <path d="M0 572 C 300 560, 650 540, 884 437 L 884 624 L 0 624 Z" fill="url(#waveFill)"/>
    </svg>

    <section class="panel panel-prp">
      <h2>PRP-Therapie</h2>
      <p>Bei der „Eigenblutbehandlung“<br>(engl. „platelet rich plasma“, PRP) wird<br>mittels spezieller Zentrifugation aus Eigen-Blut ein Plättchen-angereichertes Plasma mit einer Vielzahl von Wachstumsfaktoren gewonnen. Dieses wird dann mittels kleinster Kanülen sub- bzw. intrakutan injiziert. Typische Anwendungsbereiche sind Stimulation des Haarwachstums im Kopfbereich, Faltenbehandlung („Perlglanzkur“), Narben, Schwangerschaftsstreifen und Couperose („prominente Äderchen“).</p>
      <p>Der große Vorteil der Behandlung liegt in der Therapie mit körpereigenen Stoffen ohne Fremdmaterial. Eine Kombination mit einer „Needling-Therapie“ ist in vielen Fällen sinnvoll..</p>
      <p>Für ein ästhetisches Ergebnis sind meist<br>2-3 Sitzungen notwendig.</p>
    </section>

    <section class="panel panel-lipo">
      <h2>Lipolyse-Therapie („Fettwegspritze“)</h2>
      <p>Die Injektions-Lipolyse dient dem Abschmelzen kleinerer hartnäckiger Fettpolster (v.a. Hüpft-, Bauch-, „Reiterhosen-“, Oberarm- und Halsbereich), die durch Umstellung der Ernährung und sportliche Betätigung nicht zu beseitigen sind.</p>
      <p>Der Wirkstoff Phosphatidylcholin wird mittels feinster Nadeln direkt in das Fettgewebe injiziert. Durch die Injektionen setzt der behandelnde Arzt eine künstliche Entzündung, die eine zusätzliche Straffung der Haut bewirkt.</p>
      <p>Um ein optimales Ergebnis zu erzielen, sind 1 bis max. 4 Behandlungssitzungen notwendig, nach 6 Monaten wird der Behandlungserfolgt überprüft und ist von der Konsistenz der behandelten Fettpolster abhängig.</p>
      <p>Ca. 80% der behandelten Patienten sind mit der Behandlung sehr zufrieden. In den ersten Tagen können Schwellungen und Blutergüsse auftreten, die im Verlauf vollständig verschwinden.</p>
    </section>

    <div class="badge"><span class="badge-name">Dr. med. Stefan Duriklem</span></div>
    <div class="tagline">Ihr Arzt für Ästhetisch-kosmetische Medizin.</div>
  </main>
</body>
</html>
```